Report Cover

This is for a Binder Front, Side, Back. I have uploaded a few examples. We are an education resource company that delivers data in a format that allows districts to make better decisions. Our color palette is uploaded as well.

```html
<!DOCTYPE html>
<html lang="en">
<head>
<meta charset="utf-8">
<title>Comprehensive Needs Assessment – Maplecrest School District</title>
<link rel="stylesheet" href="https://fonts.googleapis.com/css2?family=Oswald:wght@200;300;400;500;600;700&display=swap">
<style>
  :root {
    --coral: #f2716a;
    --slate: #4d5075;
    --paper: #ffffff;
    --ink: #2b2b3a;
    --sky-deep: #4a5cd9;
    --sky-mid: #8fb0f0;
    --sky-pale: #eef2fc;
  }
  html, body {
    margin: 0;
    padding: 0;
    width: 848px;
    height: 1200px;
    overflow: hidden;
    background: var(--paper);
  }
  .cover {
    display: block;
    width: 848px;
    height: 1200px;
    font-family: "Oswald", sans-serif;
  }
  .stripe-coral { fill: var(--coral); }
  .stripe-slate { fill: var(--slate); }
  .stripe-paper { fill: var(--paper); }
  .title-box { fill: var(--coral); }
  .title-light { fill: var(--paper); font-weight: 300; font-size: 66px; }
  .title-bold { fill: var(--paper); font-weight: 600; font-size: 53px; }
  .brand-mark { fill: var(--coral); }
  .brand-name { fill: var(--ink); font-weight: 400; font-size: 24px; }
  .year { fill: var(--coral); font-weight: 200; font-size: 162px; }
  .district-name { fill: var(--slate); font-weight: 700; font-size: 130px; }
  .district-bar { fill: var(--coral); }
  .district-label { fill: var(--paper); font-weight: 500; font-size: 38px; }
</style>
</head>
<body>
<svg class="cover" viewBox="0 0 848 1200" xmlns="http://www.w3.org/2000/svg">
  <defs>
    <linearGradient id="illustration-tone" x1="0" y1="0" x2="1" y2="1">
      <stop offset="0" stop-color="var(--sky-pale)"/>
      <stop offset="0.55" stop-color="var(--sky-mid)"/>
      <stop offset="1" stop-color="var(--sky-deep)"/>
    </linearGradient>
  </defs>

  <rect class="page" width="848" height="1200" fill="var(--paper)"/>

  <!-- side chevron band -->
  <g class="side-band" transform="scale(0.62)">
    <polygon class="stripe-coral" points="42,0 182,0 182,140"/>
    <polygon class="stripe-slate" points="0,45 182,227 182,440 0,622"/>
    <polygon class="stripe-paper" points="0,290 44,335 0,380"/>
    <polygon class="stripe-coral" points="182,540 182,1330 37,940"/>
    <polygon class="stripe-slate" points="0,1250 182,1430 182,1640 0,1820"/>
    <polygon class="stripe-paper" points="0,1500 44,1545 0,1590"/>
    <polygon class="stripe-coral" points="182,1770 182,1935 0,1935"/>
  </g>

  <!-- brand -->
  <g class="brand">
    <circle class="brand-mark" cx="158" cy="113" r="12"/>
    <text class="brand-name" x="180" y="106">Learnwise</text>
    <text class="brand-name" x="180" y="138">Data, LLC</text>
  </g>

  <!-- report title -->
  <g class="report-title">
    <path class="title-box" d="M409 39 H848 V220 H409 A25 25 0 0 1 384 195 V64 A25 25 0 0 1 409 39 Z"/>
    <text class="title-light" x="429" y="131" textLength="381" lengthAdjust="spacingAndGlyphs">COMPREHENSIVE</text>
    <text class="title-bold" x="429" y="183" textLength="381" lengthAdjust="spacingAndGlyphs">NEEDS ASSESSMENT</text>
  </g>

  <!-- hero illustration area -->
  <g class="hero-illustration" role="img" aria-label="Isometric illustration of three analysts reviewing charts, dashboards and data screens on floating blue platforms">
    <rect x="150" y="300" width="680" height="470" rx="30" fill="url(#illustration-tone)"/>
  </g>

  <!-- year and district -->
  <text class="year" x="201" y="967" textLength="285" lengthAdjust="spacingAndGlyphs">2024</text>
  <text class="district-name" x="193" y="1080" textLength="607" lengthAdjust="spacingAndGlyphs">MAPLECREST</text>
  <rect class="district-bar" x="192" y="1087" width="612" height="54" rx="3"/>
  <text class="district-label" x="226" y="1132" textLength="545" lengthAdjust="spacing">SCHOOL DISTRICT</text>
</svg>
</body>
</html>
```